10x10 TradeShow Booth - Tech Conference.

Need to design a 10x10 TradeShow Booth. Designs needed by 8/22. Elements can be found on our website - www.linkrivet.example. I have access to high res logo files etc.

Our value proposition is that we work with nearly every ISP, VoIP and Cloud provider around the globe and can position the very best and most cost effective solutions from anyone, anywhere. We are trusted advisors in the IT Pro world and are 100% agnostic - focused on the client experience from pre sales to post. Dedicated to a longstanding partnership with our clients etc.

Target Market(s)

IT Professionals

Industry/Entity Type

Telecom

Font styles to use
Sans Serif

Colors
ffcf3e
0455a3

Requirements
Must have
• Elements from our website - www.linkrivet.example. We will want to showcase Logos/Partnerships that we carry - 300+ Partners etc.

```html
<!DOCTYPE html>
<html lang="en">
<head>
<meta charset="utf-8">
<title>LinkRivet – 10x10 Trade Show Booth</title>
<link rel="stylesheet" href="https://fonts.googleapis.com/css2?family=Montserrat:wght@400;500;700;800&display=swap">
<style>
  :root {
    --backdrop: #d6eef5;
    --brand-blue: #1450a0;
    --brand-orange: #f39322;
    --frame-grey: #86888b;
    --panel-white: #ffffff;
    --sky-light: #9cc3e4;
    --sky-deep: #2f6fae;
    --accent-cyan: #1da1dc;
  }
  html, body {
    margin: 0;
    padding: 0;
    width: 1200px;
    height: 1200px;
    overflow: hidden;
    background: var(--backdrop);
  }
  .booth { display: block; width: 1200px; height: 1200px; }
  .booth text { font-family: "Montserrat", Arial, sans-serif; }
  .url { font-size: 22px; font-weight: 400; fill: var(--brand-blue); }
  .brand { font-weight: 800; fill: var(--brand-blue); }
  .tagline { font-size: 26px; font-weight: 400; fill: var(--brand-orange); }
  .headline { font-weight: 800; fill: var(--brand-blue); }
  .veterans { font-size: 31px; font-weight: 500; fill: var(--brand-orange); }
  .quote-kicker { font-size: 19px; font-weight: 500; fill: var(--panel-white); letter-spacing: 1px; }
  .quote-main { font-size: 33px; font-weight: 800; fill: var(--brand-orange); letter-spacing: 1px; }
  .quote-mark { font-size: 64px; font-weight: 800; fill: var(--brand-orange); }
  .savings { font-size: 27px; font-weight: 800; fill: var(--panel-white); }
  .call { font-size: 23px; font-weight: 500; fill: var(--brand-orange); }
  .pillar-title { font-size: 18px; font-weight: 800; fill: var(--panel-white); }
  .pillar-sub { font-size: 13px; font-weight: 700; fill: var(--brand-orange); }
  .support { font-size: 21px; font-weight: 800; fill: var(--panel-white); }
  .panel-frame { fill: var(--panel-white); stroke: var(--frame-grey); stroke-width: 6; }
  .fill-blue { fill: var(--brand-blue); }
  .fill-orange { fill: var(--brand-orange); }
  .partner-badge { fill: #c9ced4; }
  .partner-badge.alt { fill: #9aa6b3; }
  .pillar-icon { fill: var(--brand-orange); stroke: var(--panel-white); stroke-width: 3; }
  .icon-line { fill: none; stroke: var(--panel-white); stroke-width: 3; stroke-linecap: round; }
  .rule-white { stroke: var(--panel-white); stroke-width: 2; fill: none; }
  .rule-orange { stroke: var(--brand-orange); stroke-width: 2.5; }
</style>
</head>
<body>
<svg class="booth" viewBox="0 0 1500 1500" xmlns="http://www.w3.org/2000/svg">
  <defs>
    <clipPath id="left-panel-shape">
      <path d="M88 1255 V410 Q88 365 130 350 L680 248 Q745 240 745 300 V1255 Z"/>
    </clipPath>
    <clipPath id="right-panel-shape">
      <path d="M752 1255 V300 Q752 240 815 248 L1370 350 Q1412 365 1412 410 V1255 Z"/>
    </clipPath>
    <linearGradient id="facade-tone" x1="0" y1="0" x2="0" y2="1">
      <stop offset="0" stop-color="var(--sky-light)"/>
      <stop offset="0.6" stop-color="var(--sky-deep)"/>
      <stop offset="1" stop-color="#1d3550"/>
    </linearGradient>
  </defs>

  <!-- Left panel -->
  <g class="panel panel-left">
    <path class="panel-frame" d="M88 1255 V410 Q88 365 130 350 L680 248 Q745 240 745 300 V1255 Z"/>
    <g clip-path="url(#left-panel-shape)">
      <polygon class="fill-blue" points="88,582 88,1258 686,1258"/>
      <polygon class="fill-orange" points="258,752 612,752 748,902 748,1258 700,1258"/>
    </g>

    <text class="url" x="706" y="333" text-anchor="end">www.linkrivet.example</text>
    <text class="brand" x="365" y="495" font-size="60" textLength="338" lengthAdjust="spacingAndGlyphs">LinkRivet</text>
    <text class="tagline" x="370" y="567">GLOBAL FOOTPRINT.</text>
    <text class="tagline" x="370" y="603">300+ SUPPLIER PARTNERS.</text>
    <text class="headline" x="365" y="667" font-size="48" textLength="336" lengthAdjust="spacingAndGlyphs">BEST PRICING</text>
    <text class="headline" x="365" y="722" font-size="48" textLength="348" lengthAdjust="spacingAndGlyphs">GUARANTEED.</text>

    <g class="partner-lens">
      <line x1="205" y1="618" x2="168" y2="652" stroke="#4a4c50" stroke-width="24" stroke-linecap="round"/>
      <line x1="176" y1="644" x2="163" y2="657" stroke="var(--accent-cyan)" stroke-width="26" stroke-linecap="butt"/>
      <circle cx="265" cy="547" r="84" fill="#ffffff" stroke="#4a4c50" stroke-width="10"/>
      <rect class="partner-badge alt" x="222" y="485" width="86" height="10" rx="2"/>
      <rect class="partner-badge" x="196" y="505" width="52" height="9" rx="2"/>
      <rect class="partner-badge alt" x="256" y="504" width="70" height="14" rx="2"/>
      <rect class="partner-badge" x="192" y="521" width="58" height="12" rx="2"/>
      <rect class="partner-badge" x="192" y="541" width="56" height="12" rx="2"/>
      <circle class="partner-badge alt" cx="272" cy="546" r="10"/>
      <rect class="partner-badge" x="292" y="542" width="44" height="12" rx="2"/>
      <rect class="partner-badge alt" x="195" y="567" width="54" height="12" rx="2"/>
      <rect class="partner-badge" x="272" y="565" width="62" height="16" rx="2"/>
      <rect class="partner-badge" x="232" y="593" width="54" height="7" rx="2"/>
      <rect class="partner-badge alt" x="226" y="606" width="70" height="9" rx="2"/>
    </g>

    <g class="quote-block">
      <text class="quote-mark" x="140" y="972">“</text>
      <line class="rule-white" x1="186" y1="939" x2="210" y2="939"/>
      <text class="quote-kicker" x="222" y="946">MORE THAN</text>
      <line class="rule-white" x1="356" y1="939" x2="380" y2="939"/>
      <polyline class="rule-white" points="380,939 380,992"/>
      <polyline class="rule-white" points="154,958 154,1010 356,1010"/>
      <text class="quote-main" x="162" y="988">BEST PRICE</text>
      <text class="quote-mark" x="358" y="1044">”</text>
    </g>

    <text class="savings" x="143" y="1068">YOU SAVE UP TO 70%</text>
    <text class="savings" x="143" y="1101">ON CONNECTIVITY,</text>
    <text class="savings" x="143" y="1135">VOICE AND CLOUD.</text>
    <text class="call" x="143" y="1193">CALL US: 1-800-555-0142</text>
  </g>

  <!-- Right panel -->
  <g class="panel panel-right">
    <path class="panel-frame" d="M752 1255 V300 Q752 240 815 248 L1370 350 Q1412 365 1412 410 V1255 Z"/>
    <g clip-path="url(#right-panel-shape)">
      <rect x="752" y="912" width="662" height="346" fill="url(#facade-tone)" role="img" aria-label="Blurred photo of a modern glass office building facade"/>
      <rect class="fill-blue" x="752" y="912" width="662" height="10"/>
      <polygon fill="var(--panel-white)" points="752,912 784,912 1078,1258 752,1258"/>
      <polygon class="fill-orange" points="752,912 768,912 1058,1258 752,1258"/>
    </g>

    <text class="url" x="800" y="333">www.linkrivet.example</text>
    <text class="brand" x="1080" y="500" font-size="96" text-anchor="middle" textLength="520" lengthAdjust="spacingAndGlyphs">LinkRivet</text>

    <text class="headline" x="1087" y="655" font-size="60" text-anchor="middle" textLength="344" lengthAdjust="spacingAndGlyphs">UNBIASED,</text>
    <text class="headline" x="1087" y="698" font-size="36" text-anchor="middle" textLength="342" lengthAdjust="spacingAndGlyphs">FREE CONSULTING</text>
    <text class="headline" x="1087" y="748" font-size="52" text-anchor="middle" textLength="342" lengthAdjust="spacingAndGlyphs">AND DESIGN</text>
    <line class="rule-orange" x1="862" y1="765" x2="1310" y2="765"/>
    <text class="veterans" x="1086" y="805" text-anchor="middle" textLength="440" lengthAdjust="spacingAndGlyphs">FROM INDUSTRY VETERANS.</text>
    <line class="rule-orange" x1="862" y1="818" x2="1310" y2="818"/>

    <g class="pillar pillar-trusted">
      <circle class="pillar-icon" cx="927" cy="918" r="32"/>
      <circle cx="914" cy="908" r="4" fill="#fff"/>
      <circle cx="927" cy="905" r="4.5" fill="#fff"/>
      <circle cx="940" cy="908" r="4" fill="#fff"/>
      <rect x="910" y="915" width="8" height="17" rx="2" fill="#fff"/>
      <rect x="922.5" y="913" width="9" height="21" rx="2" fill="#fff"/>
      <rect x="936" y="915" width="8" height="17" rx="2" fill="#fff"/>
      <text class="pillar-title" x="927" y="982" text-anchor="middle">TRUSTED</text>
      <text class="pillar-sub" x="927" y="998" text-anchor="middle">ADVISOR</text>
    </g>
    <g class="pillar pillar-global">
      <circle class="pillar-icon" cx="1116" cy="918" r="32"/>
      <circle class="icon-line" cx="1111" cy="922" r="13"/>
      <circle class="icon-line" cx="1123" cy="911" r="7"/>
      <line class="icon-line" x1="1128" y1="916" x2="1135" y2="923"/>
      <text class="pillar-title" x="1116" y="982" text-anchor="middle">GLOBAL</text>
      <text class="pillar-sub" x="1116" y="998" text-anchor="middle">REACH</text>
    </g>
    <g class="pillar pillar-tech">
      <circle class="pillar-icon" cx="1302" cy="918" r="32"/>
      <rect x="1285" y="910" width="14" height="22" fill="#fff"/>
      <rect x="1301" y="902" width="17" height="30" fill="#fff"/>
      <line x1="1288" y1="916" x2="1296" y2="916" stroke="var(--brand-orange)" stroke-width="2"/>
      <line x1="1288" y1="922" x2="1296" y2="922" stroke="var(--brand-orange)" stroke-width="2"/>
      <line x1="1309.5" y1="916" x2="1309.5" y2="927" stroke="var(--brand-orange)" stroke-width="2.5"/>
      <circle cx="1309.5" cy="911" r="1.8" fill="var(--brand-orange)"/>
      <text class="pillar-title" x="1302" y="982" text-anchor="middle">RIGHT-FIT</text>
      <text class="pillar-sub" x="1302" y="998" text-anchor="middle">TECHNOLOGY</text>
    </g>

    <text class="support" x="1352" y="1050" text-anchor="end">WORLD-CLASS POST-SALES SUPPORT</text>
    <text class="support" x="1352" y="1077" text-anchor="end">AND LIFECYCLE MANAGEMENT</text>
  </g>
</svg>
</body>
</html>
```